Glass window Vinyl

We are in need of window vinyls for the building shown in the photos. The current vinyls will come down, and we will install the new signage created by this process. We need to advertise:

"Harwell's Landing Pop Up Market"

Then, below that, it should say for rental inquiries call : 555.613.0872 with our logo which is attached along with our colors and brand guidelines. You may add more color to the Harwells landing pop up market signage if appropriate. It should be large enough to be easily read from the road by those passing by.

```html
<!DOCTYPE html>
<html lang="en">
<head>
<meta charset="utf-8">
<title>Harwell's Landing Pop Up Market – Window Vinyl</title>
<link rel="stylesheet" href="https://fonts.googleapis.com/css2?family=Bebas+Neue&display=swap">
<style>
  :root {
    --gold: #9a845c;
    --teal: #0d4351;
    --white: #fbfbfb;
    --panel-white: #ffffff;
  }
  html, body {
    margin: 0;
    padding: 0;
    width: 1200px;
    height: 1200px;
    overflow: hidden;
    background: var(--teal);
  }
  .sign {
    position: relative;
    width: 1200px;
    height: 1200px;
    background: linear-gradient(135deg, var(--gold) 0%, var(--gold) 44%, var(--teal) 53%, var(--teal) 100%);
  }
  .sign svg {
    position: absolute;
    inset: 0;
    display: block;
  }
  .headline text,
  .contact text,
  .brand text {
    font-family: "Bebas Neue", "Oswald", sans-serif;
  }
  .headline text { fill: var(--white); }
  .contact text { fill: var(--white); }
  .brand-name { fill: var(--teal); }
  .band-teal { fill: var(--teal); }
  .band-gold { fill: var(--gold); }
  .band-white { fill: var(--panel-white); }
  .brand-mark { fill: var(--gold); }
</style>
</head>
<body>
<div class="sign">
  <svg viewBox="0 0 1200 1200" width="1200" height="1200" xmlns="http://www.w3.org/2000/svg">
    <g class="headline" aria-label="Harwell's Landing Pop Up Market">
      <text x="81" y="310" font-size="282" textLength="1042" lengthAdjust="spacingAndGlyphs">HARWELL'S</text>
      <text x="81" y="510" font-size="230" textLength="1042" lengthAdjust="spacingAndGlyphs">LANDING POP UP</text>
      <text x="81" y="843" font-size="426" textLength="1042" lengthAdjust="spacingAndGlyphs">MARKET</text>
    </g>

    <g class="bands">
      <polygon class="band-teal" points="476,941 1200,941 1200,1200 551,1200"/>
      <polygon class="band-gold" points="486,941 1200,941 1200,1200 561,1200"/>
      <polygon class="band-white" points="0,983 490,983 551,1200 0,1200"/>
    </g>

    <g class="brand" aria-label="Fernbrook Row Properties">
      <rect class="brand-mark" x="249" y="1012" width="26" height="26"/>
      <text class="brand-name" x="262" y="1112" font-size="50" text-anchor="middle" letter-spacing="6">FERNBROOK ROW</text>
      <text class="brand-name" x="262" y="1160" font-size="24" text-anchor="middle" letter-spacing="7">PROPERTIES</text>
    </g>

    <g class="contact">
      <text x="1171" y="1029" font-size="50" text-anchor="end" textLength="446" lengthAdjust="spacingAndGlyphs">FOR RENTAL INQUIRIES CALL</text>
      <text x="1171" y="1161" font-size="140" text-anchor="end" textLength="592" lengthAdjust="spacingAndGlyphs">555.613.0872</text>
    </g>
  </svg>
</div>
</body>
</html>
```